Online radio: TunaWave homepage redesign

TunaWave is one of the world's leading brands of personalizable online radio -- similar to Melodex, but aimed at a somewhat older audience (age 35-54).

We'd like to redesign our homepage with a more contemporary look: It should emphasize our wide variety of GENRES (as the primary navigation), with the search field easy to find as a secondary navigation.

We'd like to retain our corporate color of maroon/plum. (We are not committed to the gold/yellow secondary color.)

See our current homepage at www.tunawave-example.com and our in-house attempt at an improved design at http://web4.tunawave-example.com/finder/2013ms/.

Ideally, we'd like to see designs for up to THREE different states:

(1) An initial state when users first come to the page.

(2) What the page would look like as the user is looking at channel options.

(3) What the page would look like once the media player is launched.

However, you may be able to combine (2) and (3) in a single screenshot.

Thanks!
Updates

At the request of several designers, we have decided to extend our deadline by four days. At the same time, we have increased our budget, including the addition of a 2nd place award. Thanks for your excellent work!

Thanks very much for your designs! We are very pleased with the overall quality of the work we are seeing. One reminder: As our brief says, the user interface "should emphasize our wide variety of GENRES (as the primary navigation), with the search field easy to find as a secondary navigation," and we feel that your design uses the SEARCH field as the primary navigation. Many of the designs use a large search field as the primary navigation. If yours does, you might want to tweak your design to put a greater emphasis on browsing genres as the primary navigation. Thanks and good luck!

Target Market(s)

Adults age 35-54 listening to online radio at work

Industry/Entity Type

Radio

Font styles to use
Sans Serif

Requirements
Must have
• This is a design/UI project -- we do not need code

```html
<!DOCTYPE html>
<html lang="en">
<head>
<meta charset="utf-8">
<title>TunaWave – Genres</title>
<link href="https://fonts.googleapis.com/css2?family=Fira+Sans:wght@400;500;600&display=swap" rel="stylesheet">
<style>
:root{
  --plum-bg:#4b1541;
  --plum-card:#5f1a50;
  --plum-frame:#4a1340;
  --teal:#1ccfd0;
  --teal-band:#00cbcb;
  --teal-deep:#005a5b;
  --pink:#f08cc4;
  --ink:#1d4d58;
  --muted:#a890a2;
}
*{margin:0;padding:0;box-sizing:border-box}
html,body{width:1200px;height:1000px;overflow:hidden}
body{background:var(--plum-bg);font-family:"Fira Sans",sans-serif;position:relative}
.genre-card{position:absolute;width:460px;height:220px;background:var(--plum-card);overflow:hidden}
.genre-card.side{opacity:.45}
.genre-title{position:absolute;left:28px;top:16px;color:var(--teal);font-size:21px;font-weight:600;letter-spacing:.2px}
.covers{position:absolute;left:30px;top:55px;display:flex;gap:20px}
.cover-frame{width:120px;height:120px;background:var(--plum-frame);padding:10px}
.cover-art{width:100px;height:100px}
.genre-link{position:absolute;left:28px;top:184px;color:var(--pink);font-size:16px;font-weight:500;text-decoration:none}
.nav-arrow{position:absolute;top:200px;width:54px;height:52px;border-radius:50%;background:var(--teal);display:flex;align-items:center;justify-content:center}
.apps-band{position:absolute;left:0;top:660px;width:1200px;height:230px;background:var(--teal-band)}
.apps-icon{position:absolute;left:120px;top:42px}
.apps-title{position:absolute;left:185px;top:40px;color:#fff;font-size:25px;font-weight:600}
.apps-text{position:absolute;left:185px;top:77px;color:var(--ink);font-size:16.5px}
.store-btn{position:absolute;top:125px;width:225px;height:60px;background:var(--teal-deep);display:flex;align-items:center;padding-left:15px}
.store-label{color:var(--teal);font-size:16px;font-weight:600;line-height:16px;width:78px}
.store-badge{width:120px;height:34px;border-radius:4px;background:#0b3c3d;border:1px solid #2a8a8a}
.site-footer{position:absolute;left:0;top:890px;width:1200px;height:110px}
.brand-mark{position:absolute;left:120px;top:20px;width:20px;height:20px;border-radius:50%;border:2px solid var(--teal)}
.copyright{position:absolute;left:151px;top:21px;color:var(--muted);font-size:14px}
.footer-links{position:absolute;right:119px;top:21px;display:flex;gap:36px}
.footer-links a{color:var(--pink);font-size:14px;text-decoration:none}
</style>
</head>
<body>

<!-- top row (partially scrolled) -->
<div class="genre-card" style="left:120px;top:-140px">
  <div class="covers">
    <div class="cover-frame"><div class="cover-art" role="img" aria-label="Album cover" style="background:linear-gradient(#8a7a6a,#4a3a30)"></div></div>
    <div class="cover-frame"><div class="cover-art" role="img" aria-label="Album cover" style="background:linear-gradient(#e8d830,#c8b800)"></div></div>
    <div class="cover-frame"><div class="cover-art" role="img" aria-label="Album cover" style="background:linear-gradient(#222,#555)"></div></div>
  </div>
  <a class="genre-link" href="#">View all stations &nbsp;in this genre ›</a>
</div>
<div class="genre-card" style="left:620px;top:-140px">
  <div class="covers">
    <div class="cover-frame"><div class="cover-art" role="img" aria-label="Album cover" style="background:linear-gradient(#e0d8b0,#b8a870)"></div></div>
    <div class="cover-frame"><div class="cover-art" role="img" aria-label="Album cover" style="background:linear-gradient(#333,#111)"></div></div>
    <div class="cover-frame"><div class="cover-art" role="img" aria-label="Album cover" style="background:linear-gradient(#5a6a70,#2a3a40)"></div></div>
  </div>
  <a class="genre-link" href="#">View all stations &nbsp;in this genre ›</a>
</div>

<!-- Classical / Country -->
<div class="genre-card" style="left:120px;top:120px">
  <h2 class="genre-title">CLASSICAL</h2>
  <div class="covers">
    <div class="cover-frame"><div class="cover-art" role="img" aria-label="Classical album cover" style="background:linear-gradient(#3a3530,#1a1815)"></div></div>
    <div class="cover-frame"><div class="cover-art" role="img" aria-label="Classical album cover" style="background:linear-gradient(#c8dce6,#7fa4b8)"></div></div>
    <div class="cover-frame"><div class="cover-art" role="img" aria-label="Classical album cover" style="background:linear-gradient(#2a2a2a,#0a0a0a)"></div></div>
  </div>
  <a class="genre-link" href="#">View all stations &nbsp;in this genre ›</a>
</div>
<div class="genre-card" style="left:620px;top:120px">
  <h2 class="genre-title">COUNTRY</h2>
  <div class="covers">
    <div class="cover-frame"><div class="cover-art" role="img" aria-label="Country album cover" style="background:linear-gradient(#4a4038,#1e1a16)"></div></div>
    <div class="cover-frame"><div class="cover-art" role="img" aria-label="Country album cover" style="background:linear-gradient(#b8b0a4,#6a6258)"></div></div>
    <div class="cover-frame"><div class="cover-art" role="img" aria-label="Country album cover" style="background:linear-gradient(#f0a040,#c06020)"></div></div>
  </div>
  <a class="genre-link" href="#">View all stations &nbsp;in this genre ›</a>
</div>

<!-- Classic Rock / Smooth Jazz -->
<div class="genre-card" style="left:120px;top:380px">
  <h2 class="genre-title">CLASSIC ROCK</h2>
  <div class="covers">
    <div class="cover-frame"><div class="cover-art" role="img" aria-label="Rock album cover" style="background:linear-gradient(#9ab0c8,#5e708a)"></div></div>
    <div class="cover-frame"><div class="cover-art" role="img" aria-label="Rock album cover" style="background:linear-gradient(#2a1a10,#c04a10)"></div></div>
    <div class="cover-frame"><div class="cover-art" role="img" aria-label="Rock album cover" style="background:linear-gradient(#e8e8e8,#888)"></div></div>
  </div>
  <a class="genre-link" href="#">View all stations &nbsp;in this genre ›</a>
</div>
<div class="genre-card" style="left:620px;top:380px">
  <h2 class="genre-title">SMOOTH JAZZ</h2>
  <div class="covers">
    <div class="cover-frame"><div class="cover-art" role="img" aria-label="Jazz album cover" style="background:linear-gradient(#c02828,#7a1010)"></div></div>
    <div class="cover-frame"><div class="cover-art" role="img" aria-label="Jazz album cover" style="background:linear-gradient(#6a6a6a,#2a2a2a)"></div></div>
    <div class="cover-frame"><div class="cover-art" role="img" aria-label="Jazz album cover" style="background:linear-gradient(#e06018,#a03010)"></div></div>
  </div>
  <a class="genre-link" href="#">View all stations &nbsp;in this genre ›</a>
</div>

<!-- side previews -->
<div class="genre-card side" style="left:-380px;top:-140px"></div>
<div class="genre-card side" style="left:-380px;top:120px">
  <div class="covers"><div></div><div></div><div class="cover-frame"><div class="cover-art" role="img" aria-label="Album cover" style="background:linear-gradient(#4a7ab8,#1a3a6a)"></div></div></div>
</div>
<div class="genre-card side" style="left:-380px;top:380px">
  <div class="covers"><div></div><div></div><div class="cover-frame"><div class="cover-art" role="img" aria-label="Album cover" style="background:linear-gradient(#b88a40,#5a3a20)"></div></div></div>
</div>
<div class="genre-card side" style="left:1120px;top:-140px"><a class="genre-link" href="#">View all stations</a></div>
<div class="genre-card side" style="left:1120px;top:120px">
  <h2 class="genre-title">METAL</h2>
  <div class="covers"><div class="cover-frame"><div class="cover-art" role="img" aria-label="Album cover" style="background:linear-gradient(#3a3a3a,#111)"></div></div></div>
  <a class="genre-link" href="#">View all stations</a>
</div>
<div class="genre-card side" style="left:1120px;top:380px">
  <h2 class="genre-title">DISCO</h2>
  <div class="covers"><div class="cover-frame"><div class="cover-art" role="img" aria-label="Album cover" style="background:linear-gradient(#6a3a6a,#2a102a)"></div></div></div>
  <a class="genre-link" href="#">View all stations</a>
</div>

<a class="nav-arrow" href="#" style="left:45px" aria-label="Previous genres">
  <svg width="14" height="18" viewBox="0 0 14 18"><path d="M11 2 L4 9 L11 16" fill="none" stroke="#0b3b46" stroke-width="4"/></svg>
</a>
<a class="nav-arrow" href="#" style="left:1105px" aria-label="Next genres">
  <svg width="14" height="18" viewBox="0 0 14 18"><path d="M3 2 L10 9 L3 16" fill="none" stroke="#0b3b46" stroke-width="4"/></svg>
</a>

<section class="apps-band">
  <svg class="apps-icon" width="52" height="60" viewBox="0 0 52 60">
    <rect x="13" y="1.5" width="37" height="57" rx="4" fill="none" stroke="#fff" stroke-width="2.5"/>
    <rect x="1.5" y="20" width="20" height="38" rx="3" fill="var(--teal-band)" stroke="#fff" stroke-width="2.5"/>
    <line x1="5" y1="26" x2="18" y2="26" stroke="#fff" stroke-width="1.5"/>
    <line x1="5" y1="51" x2="18" y2="51" stroke="#fff" stroke-width="1.5"/>
  </svg>
  <h2 class="apps-title">GET THE FREE TUNAWAVE APPS</h2>
  <p class="apps-text">In the car, at the gym, on the train, at home – take TunaWave wherever you go and always have access to your favorite channels</p>
  <div class="store-btn" style="left:120px"><span class="store-label">FONEPRO<br>SLATEPAD</span><span class="store-badge"></span></div>
  <div class="store-btn" style="left:365px"><span class="store-label">DROIDEX</span><span class="store-badge"></span></div>
  <div class="store-btn" style="left:610px"><span class="store-label">READWELL</span><span class="store-badge"></span></div>
  <div class="store-btn" style="left:855px"><span class="store-label">STREAMBOX</span><span class="store-badge"></span></div>
</section>

<footer class="site-footer">
  <span class="brand-mark"></span>
  <p class="copyright">© Copyright 2014 Northfold Studio</p>
  <nav class="footer-links"><a href="#">Legal</a><a href="#">Privacy</a><a href="#">Cookies</a></nav>
</footer>

</body>
</html>
```